Creative Web Design - Intl Market Research Company

We need an innovative web design for an emerging company into the international market research marketplace.

The company, Velmoran Associates, is a Trade, Investment, and Market Research company. Velmoran offers domestic and international companies increased success in the U.S. marketplace by providing a variety of services. (seen on attached brochure)

The website should be cutting edge and creative while having an easy navigation. The color is not fixed and attached logo is not finalized, feel free to post anything from conservative to progressive options. Keep in mind target customers are domestic and international businesses looking to emerge/improve in the U.S. marketplace.

Additional Company information is located in the attached documentation. The documentation is outdated & winner will have priority standing for our next projects.(logo & document re-design)
Updates

I have received a few e-mail requests and have updated the status to guaranteed payment.

Thanks!

Target Market(s)

Any company, foreign and domestic, looking to introduce their product into the U.S. marketplace.

Industry/Entity Type

Market Research

Requirements
Must have
• Easy Navigation
Should not have
• Too many buttons
Difficult navigation
Excessive Typography

```html
<!DOCTYPE html>
<html lang="en">
<head>
<meta charset="utf-8">
<title>Velmoran Associates — Trade, Investment, Market Research</title>
<link href="https://fonts.googleapis.com/css2?family=Raleway:wght@300;400;500;600;700;800&family=Special+Elite&family=Damion&display=swap" rel="stylesheet">
<style>
  :root{
    --ink:#111111;
    --text:#2a2a2a;
    --muted:#5a5a5a;
    --gold:#c9a23a;
    --gold-dark:#a8831f;
    --panel:#f3f2ee;
    --panel-line:#d8d6d0;
    --stripe-a:#f1f0ea;
    --stripe-b:#e4e2da;
    --paper:#ffffff;
    --map:#d9d9d9;
  }
  *{margin:0;padding:0;box-sizing:border-box}
  html,body{width:1200px;height:1064px;overflow:hidden;background:var(--paper)}
  body{position:relative;font-family:"Raleway",Arial,sans-serif;color:var(--text)}
  .abs{position:absolute}

  .stripe{left:0;width:1200px;background:repeating-linear-gradient(135deg,var(--stripe-a) 0 3px,var(--stripe-b) 3px 5px)}
  .stripe-top{top:0;height:6px}
  .stripe-footer{top:924px;height:42px;border-bottom:1px solid var(--panel-line)}

  .brand{left:186px;top:28px;display:flex;align-items:center;gap:14px}
  .brand-name{font-family:"Raleway",sans-serif;font-weight:800;font-size:38px;color:var(--ink);letter-spacing:-0.5px}
  .brand-mark{width:34px;height:34px;border-radius:50%;background:var(--gold)}

  .social{left:906px;top:32px;display:flex;gap:10px}
  .social span{width:20px;height:22px;background:#555;border-radius:3px}

  .tagline{left:583px;top:76px;width:438px;text-align:right;font-family:"Special Elite",monospace;font-size:22px;letter-spacing:1px;color:var(--ink)}

  .nav{left:490px;top:131px;display:flex;gap:14px;font-size:15px;font-weight:500;color:var(--ink)}
  .nav .sep{color:var(--ink)}

  .map{left:172px;top:180px;width:860px;height:350px;border-radius:40% 45% 35% 40%;background:radial-gradient(ellipse at 50% 45%,#e2e2e2 0%,#ececec 55%,rgba(255,255,255,0) 75%)}
  .portrait{left:736px;top:186px;width:286px;height:343px;border-radius:120px 120px 0 0;background:linear-gradient(180deg,#c9a48a 0%,#8b6a58 22%,#3a3a3d 45%,#1f1f22 100%)}

  .headline{left:160px;top:248px;width:600px;text-align:center;color:#2b2b2b;line-height:1}
  .headline .light{display:block;font-weight:300;font-size:50px}
  .headline .bold{display:block;font-weight:700;font-size:39px;color:var(--ink);margin:5px 0 6px;letter-spacing:-0.3px}

  .process{left:181px;top:527px;width:841px;height:128px;background:var(--panel);border:1px solid var(--panel-line);border-top:none}
  .step{top:442px;width:220px;text-align:center}
  .step svg{display:block;margin:0 auto}
  .step p{margin-top:15px;font-size:20px;line-height:23px;color:#333}

  .about{left:199px;top:694px;width:390px}
  .section-name{font-family:"Raleway",sans-serif;font-weight:800;font-size:30px;color:var(--ink)}
  .about p{margin-top:10px;font-family:Arial,Helvetica,sans-serif;font-size:12.5px;line-height:18px;color:#222}
  .badges{left:186px;top:818px;width:398px;height:59px;border:1px solid #cfcfcf;background:linear-gradient(180deg,#ffffff,#f3f3f3);display:flex;align-items:center;justify-content:space-around;padding:0 20px}
  .badge{height:16px;background:#c4c4c4;border-radius:3px}
  .badge.round{width:26px;height:26px;border-radius:50%}

  .services{left:614px;top:692px;width:420px}
  .services h2{font-family:"Damion",cursive;font-weight:400;font-size:40px;color:var(--ink);line-height:1}
  .services .lead{margin-top:8px;font-size:17px;font-weight:500;color:var(--ink)}
  .service-cols{display:flex;margin-top:26px;font-size:16.5px;color:var(--muted);line-height:23.5px}
  .service-cols ul{list-style:none}
  .service-cols ul:first-child{width:225px}
  .indent{padding-left:14px}

  .footer-links{left:199px;top:990px;font-family:Arial,Helvetica,sans-serif;font-size:11px;color:#222}
  .footer-links span{margin:0 6px}
  .copyright{left:199px;top:1017px;font-family:Arial,Helvetica,sans-serif;font-size:11px;color:#222}
  .footer-brand{left:720px;top:990px;display:flex;align-items:center;gap:12px}
  .footer-brand .brand-name{font-size:30px}
  .footer-brand .brand-mark{width:28px;height:28px}
</style>
</head>
<body>
  <div class="abs stripe stripe-top"></div>

  <header>
    <div class="abs brand">
      <span class="brand-name">Velmoran Associates</span>
      <span class="brand-mark"></span>
    </div>
    <div class="abs social" aria-label="Social links"><span></span><span></span><span></span><span></span></div>
    <div class="abs tagline">TRADE,INVESTMENT,MARKET RESEARCH</div>
    <nav class="abs nav">
      <span>HOME</span><span class="sep">/</span>
      <span>ABOUT</span><span class="sep">/</span>
      <span>BLOG</span><span class="sep">/</span>
      <span>CONTACT US</span><span class="sep">/</span>
      <span>REQUEST QUOTE</span>
    </nav>
  </header>

  <section class="hero">
    <div class="abs map" role="img" aria-label="Dotted world map in light grey"></div>
    <div class="abs process"></div>
    <div class="abs portrait" role="img" aria-label="Businessman in a dark pinstripe suit and blue tie"></div>
    <h1 class="abs headline">
      <span class="light">MEETING YOUR</span>
      <span class="bold">BUSINESS INFORMATION NEEDS</span>
      <span class="light">ACROSS THE GLOBE.</span>
    </h1>

    <div class="abs step" style="left:181px">
      <svg width="138" height="138" viewBox="0 0 138 138">
        <circle cx="69" cy="69" r="69" fill="#000"/>
        <circle cx="69" cy="69" r="52" fill="none" stroke="var(--gold)" stroke-width="7"/>
        <circle cx="69" cy="69" r="34" fill="none" stroke="var(--gold)" stroke-width="7"/>
        <circle cx="69" cy="69" r="16" fill="var(--gold)"/>
      </svg>
      <p>Research<br>Appropriate Firms</p>
    </div>
    <div class="abs step" style="left:383px">
      <svg width="138" height="138" viewBox="0 0 138 138">
        <circle cx="69" cy="69" r="69" fill="#000"/>
        <path d="M32 36 V104 H108" fill="none" stroke="var(--gold)" stroke-width="6"/>
        <polyline points="40,90 58,62 78,76 104,44" fill="none" stroke="var(--gold)" stroke-width="6"/>
        <circle cx="58" cy="62" r="7" fill="var(--gold)"/>
        <circle cx="78" cy="76" r="7" fill="var(--gold)"/>
        <polygon points="94,38 112,34 108,52" fill="var(--gold)"/>
      </svg>
      <p>Present Your<br>Product/Service</p>
    </div>
    <div class="abs step" style="left:585px">
      <svg width="138" height="138" viewBox="0 0 138 138">
        <circle cx="69" cy="69" r="69" fill="#000"/>
        <g fill="none" stroke="var(--gold)" stroke-width="6">
          <circle cx="69" cy="69" r="46"/>
          <ellipse cx="69" cy="69" rx="20" ry="46"/>
          <line x1="69" y1="23" x2="69" y2="115"/>
          <line x1="23" y1="69" x2="115" y2="69"/>
          <path d="M30 46 H108 M30 92 H108"/>
        </g>
      </svg>
      <p>Select Potential<br>Matches</p>
    </div>
    <div class="abs step" style="left:788px">
      <svg width="138" height="138" viewBox="0 0 138 138">
        <circle cx="69" cy="69" r="69" fill="#000"/>
        <g fill="none" stroke="var(--gold)" stroke-width="5">
          <path d="M42 56 A34 34 0 0 1 58 38"/>
          <path d="M80 38 A34 34 0 0 1 96 56"/>
          <path d="M50 96 A34 34 0 0 0 88 96"/>
        </g>
        <circle cx="69" cy="32" r="15" fill="var(--gold)"/>
        <circle cx="36" cy="86" r="15" fill="var(--gold)"/>
        <circle cx="102" cy="86" r="15" fill="var(--gold)"/>
      </svg>
      <p>Introduce You to<br>Companies</p>
    </div>
  </section>

  <section class="abs about">
    <div class="section-name">Velmoran Associates</div>
    <p>The world is fast becoming a global economy and<br>businesses wanting to succeed in this highly competitive environment<br>must have access to upto-date business information.</p>
  </section>
  <div class="abs badges" aria-label="Partner badges">
    <span class="badge" style="width:88px"></span>
    <span class="badge" style="width:66px"></span>
    <span class="badge round"></span>
    <span class="badge" style="width:64px"></span>
  </div>

  <section class="abs services">
    <h2>List Services</h2>
    <p class="lead">Fast and Accurate Lists of:</p>
    <div class="service-cols">
      <ul>
        <li>* Importers</li>
        <li>* Agents/Representatives</li>
        <li>* Distributors</li>
        <li>* Manufacturers</li>
      </ul>
      <ul>
        <li>* Joint Venture Partners</li>
        <li>* Manufacturing Under</li>
        <li class="indent">License Partners</li>
        <li>* Investment Partners</li>
      </ul>
    </div>
  </section>

  <div class="abs stripe stripe-footer"></div>
  <footer>
    <div class="abs footer-links">Velmoran Associates<span>|</span>Recruitment<span>|</span>Press<span>|</span>Imprint<span>|</span>Contact Us</div>
    <div class="abs copyright">© 2013 &nbsp;Velmoran Associates Ltd - All Rights Reserved.</div>
    <div class="abs footer-brand">
      <span class="brand-name">Velmoran Associates</span>
      <span class="brand-mark"></span>
    </div>
  </footer>
</body>
</html>
```